"The Summit Hour Audio Series" needs 3 banner ad designs

I am seeking the design and creation of 3 differently-designed ”banner ads.” I want them to look as though there is a relation between designs but I don't want them to look the same.
While compatibility is desired, that desire should not be interpreted as sameness.

I need a series of banner ads to be a supplement and a complement to
"The Summit Hour"'s main banner ad page and accompanying site.
http://www.quorvale.org/

I am looking for high quality, creative capturing of banner ads that focus on three topic areas, namely, my:

1. Leadership Coaching Program –
“Stride Builder Mentoring Track™”

2. Training program – “The Craft of a Steady Captain”

and

3. Speaker Interest & Availability banner ad.

It is desired that each banner, and the banners collectively, complement and fit in with the look and feel of the existing, principal banner and the show’s vision and mission. (in the attachment, I have included a copy of this banner for your information).

The final design should commit experience, competence, depth and reliability.

To provide a bit of context for this request, I have included the show's vision and mission statement as well as a brief description of my perspective on each banner ad.

I will of course, provide the winner all of the information, documents, graphic depictions, etc that I have available (during the handover stage) that will enable them to create quality products.

In addition, each banner ad should be delivered as JPEG files in dimensions 728 pixel wide and 90 pixels high each. The following fonts: Trajan Pro Regular or Thomas Condensed Regular are the desired fonts.

The task summary: Design 3 banner ads as described below:

1. Leadership Coaching Program – Stride Builder Mentoring Track™
My coaching program has a formal structure that has an existing graphic capturing of leadership coaching that that would/should be incorporated in the ad.

2. Training program – The Craft of a Steady Captain
The skills training program description I have included as noted below; it is a program that can also be licensed for use by customers who would wish to use it in their organization. In addition to the creative thinking of graphics artists, it would probably be useful to view the home page graphic at www.tovrik4.com. This image might be useful in enhancing the banner ad graphic.

3. Speaking Interest – Availability
Have been and desire using this banner to communicate my interest in generating value and availability as a speaker.

-Vision-
“The Summit Hour”
Making an Impact through Effective Leadership
*is a powerfully engaging platform for great conversations about leadership and leadership learning.

-Mission-
Build a community of listeners who are informed and enthusiastically engaged with the host and the show’s goal of improving the quality of leadership wherever listeners are living and leading.

File: "1785 Postcard V2" - *this information is for use in designing the
Leadership Coaching Banner Ad* = *Stride Builder Mentoring Track*

File: "Cover Shot of Skills Book" - *this information is
for use in designing the Book Ad – The Craft of a Steady Captain:
Growing a Guide Whom Peers Gladly Trust*

File: (word doc) The Craft of a Steady Captain Training Workshop – Skills &
Concepts Summary *this information is for the design of the banner ad for
the Skills Training Course. It includes quotes that could be excerpted to
include in the banner ad*

File name: "Cover - Craft of a Steady Captain"
-> Picture of book for Craft of a Steady Captain Training Program – *this is additional information for the use in designing the Training program banner ad

You can find the other attachments useful. Please have a look.
I welcome all your creative and original designs. Remember, these are 3 different-looking banner ads - though related in some way.

Project Deadline Extended Reason: The current designs have not included enough variety and creativity. While I am desirous of compatibility of the ad renditions with the central image, I am not interpreting compatibility with sameness of looking to see the same image in each banner ad. I rather think the image differentiation promotes both interest and distinction between the products of book, leadership coaching, speaking, etc. Same image embedded in each banner ad doesn't provide the variety that I think both distinguishes and draws interest. In this regard, most of the current examples include the same pictorial images across designs and the use of just words vs. images from among those provided, As an example a picture of my book on the book banner ad seems more impactful than merely using the words book on the ad for the book; and the picture of a speaker vs. Speaker Availability.I hope this feedback is helpful . Regards,Leopold Added Saturday, June 3, 2017

Target Market(s)

Online Radio Listeners Can Visit WavelineHub.com for examples - Will be broadcast on the Commerce Channel

Industry/Entity Type

Business Consultant

Colors

Designer to choose colors to be used in the design.

Requirements
Should not have
• Anything that doesn't speak to the characteristics noted at the end of the summary provided in the description above

```html
<!DOCTYPE html>
<html lang="en">
<head>
<meta charset="utf-8">
<title>Banner Series – Leopold E. Ashcombe</title>
<link rel="stylesheet" href="https://fonts.googleapis.com/css2?family=Cinzel:wght@400;500&display=swap">
<style>
  :root {
    --stage: #000000;
    --band-deep: #93aaa6;
    --band-mid: #a9bcb9;
    --band-light: #e4ebea;
    --ink-light: #ffffff;
    --ink-dark: #1c1c1c;
    --bubble: #ffffff;
    --art-red: #c9302c;
    --art-grey: #6f6f6f;
    --art-road: #4a4a48;
    --portrait-skin: #6b4a36;
    --portrait-shirt: #e8dcc0;
  }
  html, body {
    margin: 0;
    padding: 0;
    width: 1200px;
    height: 902px;
    overflow: hidden;
    background: var(--stage);
  }
  .stage {
    position: relative;
    width: 1200px;
    height: 902px;
    background: var(--stage);
    font-family: "Cinzel", "Trajan Pro", serif;
  }
  .banner {
    position: absolute;
    left: 86px;
    width: 1028px;
    height: 127px;
    overflow: hidden;
    background:
      radial-gradient(ellipse 340px 110px at 300px 50%, var(--band-light) 0%, rgba(228,235,234,0) 100%),
      linear-gradient(90deg, var(--band-mid) 0%, var(--band-deep) 100%);
  }
  .banner--coaching { top: 184px; }
  .banner--training { top: 388px; }
  .banner--speaking { top: 596px; }

  .art {
    position: absolute;
    top: 0;
    height: 127px;
  }
  .art--leaders {
    left: 0;
    width: 150px;
    background: linear-gradient(120deg, rgba(255,255,255,0) 0%, rgba(255,255,255,0.7) 40%, rgba(255,255,255,0) 100%),
                linear-gradient(90deg, #2b2b2b 0%, var(--art-red) 70%, rgba(201,48,44,0) 100%);
    opacity: 0.85;
  }
  .art--road {
    left: 0;
    width: 184px;
    background: linear-gradient(90deg, var(--art-road) 0%, #7a7a76 70%, rgba(169,188,185,0) 100%);
  }
  .art--road::after {
    content: "";
    position: absolute;
    left: 0; right: 40px; top: 55px; height: 14px;
    background: linear-gradient(90deg, var(--art-red), rgba(201,48,44,0));
  }
  .art--presenter {
    left: 0;
    width: 130px;
    background: radial-gradient(ellipse 50px 60px at 55px 60%, #d6d6d6 0%, #b8b8b8 60%, rgba(184,184,184,0) 100%);
  }
  .art--portrait {
    right: 0;
    width: 150px;
    background: linear-gradient(90deg, rgba(169,188,185,0) 0%, var(--portrait-skin) 35%, var(--portrait-shirt) 100%);
  }

  .headline, .subline, .kicker, .signature, .bubble-text {
    position: absolute;
    margin: 0;
    font-weight: 400;
    white-space: nowrap;
    line-height: 1;
  }
  .headline {
    color: var(--ink-light);
    text-shadow: 0 1px 2px rgba(0,0,0,0.25);
  }
  .banner--coaching .headline {
    left: 243px;
    top: 20px;
    font-size: 29px;
    letter-spacing: 1px;
  }
  .subline {
    left: 243px;
    top: 57px;
    font-size: 18.5px;
    color: var(--ink-dark);
    letter-spacing: 0.6px;
  }
  .subline sup { font-size: 8px; vertical-align: 9px; }
  .kicker {
    left: 243px;
    top: 23px;
    font-size: 20px;
    color: var(--ink-dark);
    letter-spacing: 0.5px;
  }
  .banner--training .headline {
    left: 210px;
    top: 46px;
    font-size: 31px;
    letter-spacing: 0.8px;
  }
  .signature {
    right: 189px;
    top: 103px;
    font-size: 10px;
    font-weight: 500;
    color: var(--ink-dark);
    letter-spacing: 0.4px;
  }
  .banner--training .signature { top: 99px; }
  .banner--speaking .signature { top: 100px; }

  .bubble {
    position: absolute;
    left: 110px;
    top: 0;
    width: 740px;
    height: 90px;
  }
  .bubble-text {
    left: 212px;
    top: 30px;
    font-size: 30px;
    color: var(--ink-dark);
    letter-spacing: 0.6px;
  }
</style>
</head>
<body>
<main class="stage">

  <section class="banner banner--coaching" aria-label="Leadership Coaching Program banner">
    <div class="art art--leaders" role="img" aria-label="Illustration of a leader figure pointing ahead of a line of followers on a red arrow"></div>
    <h2 class="headline">Leadership Coaching Program</h2>
    <p class="subline">Stride Builder Mentoring Track<sup>™</sup></p>
    <p class="signature">Leopold E. Ashcombe</p>
    <div class="art art--portrait" role="img" aria-label="Portrait photograph of the host"></div>
  </section>

  <section class="banner banner--training" aria-label="Training Program banner">
    <div class="art art--road" role="img" aria-label="Illustration of a road with arrows, one red arrow leading"></div>
    <p class="kicker">Training Program</p>
    <h2 class="headline">The Craft of a Steady Captain</h2>
    <p class="signature">Leopold E. Ashcombe</p>
    <div class="art art--portrait" role="img" aria-label="Portrait photograph of the host"></div>
  </section>

  <section class="banner banner--speaking" aria-label="Speaking Interest and Availability banner">
    <div class="art art--presenter" role="img" aria-label="Illustration of a presenter figure with open arms"></div>
    <svg class="bubble" viewBox="0 0 740 90" aria-hidden="true">
      <path d="M110 0 H700 Q738 0 738 44 Q738 88 700 88 H110 Q84 88 78 70 L36 62 L80 48 L80 20 Q84 0 110 0 Z" fill="var(--bubble)"/>
    </svg>
    <h2 class="bubble-text">Speaking Interest &amp; Availability</h2>
    <p class="signature">Leopold E. Ashcombe</p>
    <div class="art art--portrait" role="img" aria-label="Portrait photograph of the host"></div>
  </section>

</main>
</body>
</html>
```